Building quality affordable homes in Brisbane, Australia for investors and families

We design, build and market our own homes from small single story to large 3 story luxury homes. Our main focus is "duel key" - that is two houses on one lot - a "zooky" (as in where The Zook lived) or attached granny flat.
We have a logo design and need a business card to suit. Something simple but eye catching. We want to communicate: "you are making a smart financial choice buying or building with us".
Unfortunately a lot of information has to be on the card including - Name, position, phone, mobile, fax, email, web address and of course the logo.
Logo in multiple formats and high res now available.

Target Market(s)

Families, contractors, real estate agents, other builders, developers, banks and home buyers.

Industry/Entity Type

Financial

Contact Information for Business Card

Name, position, phone, mobile, fax, email, web address

Font styles to use
Serif

Requirements
Must have
• The logo, and the details.
Nice to have
• Show or explain what we do - design, build and market affordable homes.
Should not have
• Nothing too fancy, outrageous - building companies are normally very straight.

```html
<!DOCTYPE html>
<html lang="en">
<head>
<meta charset="utf-8">
<title>Brightlot Homes – Business Card</title>
<link href="https://fonts.googleapis.com/css2?family=Open+Sans:wght@400;600;700&display=swap" rel="stylesheet">
<style>
  :root {
    --page-bg: #e9e6e1;
    --card-white: #ffffff;
    --card-white-edge: #eef3f7;
    --brand-blue: #1a7fc1;
    --brand-cyan: #3fb6dc;
    --navy-deep: #0b3f7a;
    --navy-mid: #1560a8;
    --ink: #3c3c3c;
    --ink-soft: #6f6f6f;
    --rule: #8fc4e4;
  }
  * { box-sizing: border-box; margin: 0; padding: 0; }
  html, body { width: 1200px; height: 1023px; overflow: hidden; }
  body {
    background: var(--page-bg);
    font-family: "Open Sans", Arial, sans-serif;
    display: flex;
    align-items: center;
    justify-content: center;
    gap: 50px;
  }
  .card {
    width: 540px;
    height: 330px;
    border-radius: 18px;
    position: relative;
    overflow: hidden;
    box-shadow: 0 8px 24px rgba(0,0,0,0.18);
  }

  /* Front */
  .card-front {
    background: linear-gradient(160deg, var(--card-white) 55%, var(--card-white-edge));
    color: var(--ink);
  }
  .front-web {
    position: absolute; top: 26px; right: 30px;
    color: var(--brand-blue); font-size: 13px; font-weight: 600;
  }
  .front-brand {
    position: absolute; top: 58px; left: 36px;
    display: flex; align-items: center; gap: 12px;
  }
  .brand-mark {
    width: 44px; height: 44px; background: var(--brand-cyan); border-radius: 4px;
  }
  .brand-name {
    color: var(--brand-blue); font-size: 34px; font-weight: 700; line-height: 1;
  }
  .brand-sub {
    color: var(--brand-blue); font-size: 12px; font-weight: 400;
    letter-spacing: 0.5px; margin-top: 4px; text-transform: uppercase;
  }
  .front-divider {
    position: absolute; left: 36px; right: 36px; top: 128px;
    border-top: 1px solid var(--rule);
  }
  .person {
    position: absolute; top: 142px; left: 36px;
  }
  .person-name {
    color: var(--brand-blue); font-size: 18px; font-weight: 600;
    letter-spacing: 0.5px; text-transform: uppercase;
  }
  .person-role { color: var(--ink-soft); font-size: 13px; }
  .contacts {
    position: absolute; top: 196px; left: 36px; list-style: none;
  }
  .contacts li {
    display: flex; align-items: center; gap: 9px;
    font-size: 13.5px; color: var(--ink-soft); line-height: 21px;
  }
  .contact-icon { width: 13px; height: 13px; flex: none; }
  .address {
    position: absolute; bottom: 20px; left: 36px;
    font-size: 13px; font-weight: 700; color: var(--ink);
    text-transform: uppercase; letter-spacing: 0.3px;
  }

  /* Back */
  .card-back {
    background: linear-gradient(135deg, var(--navy-mid) 0%, var(--navy-deep) 100%);
    color: #fff;
  }
  .back-mark {
    position: absolute; top: 40px; left: 40px;
    width: 52px; height: 52px; background: var(--brand-cyan); border-radius: 4px;
  }
  .back-brand {
    position: absolute; left: 40px; bottom: 40px;
  }
  .back-name {
    font-size: 46px; font-weight: 700; line-height: 1; color: #fff;
  }
  .back-sub {
    color: var(--brand-cyan); font-size: 14px; letter-spacing: 1px;
    text-transform: uppercase; margin-top: 8px;
  }
  .back-tagline {
    color: #fff; font-size: 13px; margin-top: 4px;
  }
</style>
</head>
<body>
  <section class="card card-front" aria-label="Business card front">
    <div class="front-web">www.brightlothomes.com.au</div>
    <div class="front-brand">
      <div class="brand-mark"></div>
      <div>
        <div class="brand-name">Brightlot</div>
        <div class="brand-sub">Homes Pty Ltd</div>
      </div>
    </div>
    <div class="front-divider"></div>
    <div class="person">
      <div class="person-name">Jamie Harlow</div>
      <div class="person-role">Director</div>
    </div>
    <ul class="contacts">
      <li>
        <svg class="contact-icon" viewBox="0 0 13 13"><rect width="13" height="13" rx="2" fill="#1a7fc1"/><path d="M4 3.2c.6 2.8 2.6 5.2 5.8 6.6l.6-1.4-1.6-.8-.7.7C6.9 7.6 5.8 6.5 5.2 5.3l.7-.7-.8-1.6z" fill="#fff"/></svg>
        0400 118 226
      </li>
      <li>
        <svg class="contact-icon" viewBox="0 0 13 13"><rect width="13" height="13" rx="2" fill="#1a7fc1"/><rect x="4.3" y="2.5" width="4.4" height="8" rx="0.8" fill="#fff"/></svg>
        0733 904 517
      </li>
      <li>
        <svg class="contact-icon" viewBox="0 0 13 13"><rect width="13" height="13" rx="2" fill="#1a7fc1"/><rect x="3" y="5" width="7" height="5" fill="#fff"/><rect x="4.3" y="2.6" width="4.4" height="2.4" fill="#fff"/></svg>
        0733 904 529
      </li>
      <li>
        <svg class="contact-icon" viewBox="0 0 13 13"><rect width="13" height="13" rx="2" fill="#1a7fc1"/><rect x="2.5" y="4" width="8" height="5.5" fill="#fff"/><path d="M2.5 4l4 3 4-3" stroke="#1a7fc1" stroke-width="0.8" fill="none"/></svg>
        jamie@brightlothomes.com.au
      </li>
    </ul>
    <div class="address">27 Sample Lane, Somewhere, Any City</div>
  </section>

  <section class="card card-back" aria-label="Business card back">
    <div class="back-mark"></div>
    <div class="back-brand">
      <div class="back-name">Brightlot</div>
      <div class="back-sub">Homes Pty Ltd</div>
      <div class="back-tagline">Design | Build | Market Affordable Homes</div>
    </div>
  </section>
</body>
</html>
```